Package for my report covers: Kasbury Report Covers - 11x17

Packaging design single color will be screen printed on corrugated package. I will send photos of product as well as all the key features. Want a modern/corporate design that sells the product. Same packaging will be use to sell the variety of colors, and panel materials available. Will use a small barcode label (i have) to distinguish the color/material. You can see this product on my ecommerce website at: https://www.folioplex.com/5263/ will send example of current packaging of another product

Package size will be
Inside Length: 18.625"
Inside Width: 11.625"
Inside Height: 1.25"

Target Market(s)

Engineers, CAD Drafters, Business Professionals

Industry/Entity Type

Business Management

Font styles to use
Sans Serif

Colors
0455a3

Requirements
Must have
• Single Color Design, area for barcode
Nice to have
• lost of empty area (not overwhelming)
Should not have
• Profanities, sex,

```html
<!DOCTYPE html>
<html lang="en">
<head>
<meta charset="utf-8">
<title>Kasbury Report Covers – Package</title>
<link href="https://fonts.googleapis.com/css2?family=Josefin+Sans:wght@300;400&display=swap" rel="stylesheet">
<style>
  :root {
    --brand-blue: #0455a3;
    --sheet-white: #ffffff;
    --tint-light: #eef1f6;
    --tint-mark: rgba(255, 255, 255, 0.14);
    --backdrop: #d9dadc;
  }
  * { margin: 0; padding: 0; box-sizing: border-box; }
  html, body {
    width: 1200px; height: 960px; overflow: hidden;
    background: var(--backdrop);
    font-family: "Josefin Sans", sans-serif;
  }
  .package {
    position: absolute; left: 265px; top: 40px;
    width: 670px; height: 880px;
    display: flex;
    background: var(--sheet-white);
    box-shadow: 0 10px 30px rgba(0,0,0,0.18);
  }
  /* Spine */
  .spine {
    position: relative; width: 96px; height: 100%;
    background: var(--sheet-white);
  }
  .spine-pattern {
    position: absolute; left: 30px; top: 0; width: 66px; height: 520px;
    background: var(--tint-light);
  }
  .spine-band {
    position: absolute; left: 0; top: 0; width: 30px; height: 100%;
    background: var(--brand-blue);
  }
  .spine-title {
    position: absolute; left: 4px; bottom: 168px;
    writing-mode: vertical-rl; transform: rotate(180deg);
    color: var(--sheet-white); font-weight: 300;
    font-size: 22px; letter-spacing: 2px; text-transform: uppercase;
    white-space: nowrap; line-height: 1;
  }
  .spine-web {
    position: absolute; left: 52px; bottom: 18px;
    writing-mode: vertical-rl; transform: rotate(180deg);
    color: var(--brand-blue); font-size: 11px; letter-spacing: 3.2px;
    text-transform: uppercase; white-space: nowrap; line-height: 1;
  }
  /* Front */
  .front {
    position: relative; width: 574px; height: 100%;
    background: var(--sheet-white);
    overflow: hidden;
  }
  .front-pattern {
    position: absolute; left: 0; top: 0; width: 100%; height: 194px;
    background: var(--tint-light);
  }
  .front-panel {
    position: absolute; left: 0; top: 194px; right: 0; bottom: 0;
    border-top-left-radius: 44px;
    background: var(--brand-blue);
  }
  .front-monogram {
    position: absolute; left: 40px; top: 600px; width: 440px; height: 280px;
    border-top-left-radius: 140px;
    background: var(--tint-mark);
  }
  .brand-dot {
    position: absolute; left: 201px; top: 112px; width: 160px; height: 160px;
    border-radius: 50%;
    background: var(--sheet-white);
    border: 20px solid var(--brand-blue);
  }
  .brand-name {
    position: absolute; left: 0; right: 0; top: 290px;
    text-align: center; color: var(--sheet-white);
    font-weight: 300; font-size: 54px; letter-spacing: 4px; line-height: 1;
    text-transform: uppercase;
  }
  .product-line {
    position: absolute; left: 0; right: 0; top: 350px;
    text-align: center; color: var(--sheet-white);
    font-weight: 300; font-size: 32px; letter-spacing: 0.5px; line-height: 1;
    text-transform: uppercase;
  }
  .edition-year {
    position: absolute; left: 135px; top: 704px;
    color: var(--sheet-white); font-weight: 300; font-size: 40px; line-height: 1;
  }
  .barcode-area {
    position: absolute; right: 28px; bottom: 28px;
    width: 130px; height: 70px;
    background: var(--sheet-white);
  }
</style>
</head>
<body>
  <div class="package">
    <aside class="spine">
      <div class="spine-pattern" role="img" aria-label="Light geometric triangle pattern"></div>
      <div class="spine-band"></div>
      <div class="spine-title">Kasbury Report Covers</div>
      <div class="spine-web">www.websiteaddress.com</div>
    </aside>
    <section class="front">
      <div class="front-pattern" role="img" aria-label="Light geometric triangle pattern"></div>
      <div class="front-panel"></div>
      <div class="front-monogram" role="img" aria-label="Large decorative brand initial"></div>
      <div class="brand-dot"></div>
      <h1 class="brand-name">Kasbury</h1>
      <p class="product-line">Report Covers</p>
      <p class="edition-year">2018</p>
      <div class="barcode-area" aria-label="Space for barcode label"></div>
    </section>
  </div>
</body>
</html>
```